We Need a GREAT Looking Sales Flyer!

Our small, boutique fitness facility needs a new flyer which highlights a new entry level fitness program that we are launching.

The flyer should be visually appealing as we will be handing a full color version to the potential member during our sales process.

I have attached:
- a word document which includes text
-Photos that can be used. Not all need to be used. These are to be used as you feel appropriate
- Our Logo

```html
<!DOCTYPE html>
<html lang="en">
<head>
<meta charset="utf-8">
<title>Northline Fitness – The Ultimate Kickstart Flyer</title>
<link rel="stylesheet" href="https://fonts.googleapis.com/css2?family=Montserrat:wght@400;600;700;800&family=Oswald:wght@500;700&display=swap">
<style>
  :root {
    --backdrop: #7d98c4;
    --brand-blue: #1677cc;
    --logo-blue: #1a6fc9;
    --lime: #b8dc1e;
    --paper: #f4f4f4;
    --ink: #1c1c1c;
    --photo-dark: #2a2b3a;
    --photo-violet: #5a56c8;
  }
  * { margin: 0; padding: 0; box-sizing: border-box; }
  html, body {
    width: 1200px;
    height: 840px;
    overflow: hidden;
    background: var(--backdrop);
  }
  .flyer {
    position: absolute;
    left: 290px;
    top: 20px;
    width: 620px;
    height: 800px;
    overflow: hidden;
    background: var(--brand-blue);
    font-family: "Montserrat", Arial, sans-serif;
  }
  .flyer-shapes {
    position: absolute;
    inset: 0;
    width: 620px;
    height: 800px;
  }
  .flyer-text { position: absolute; }

  .headline {
    left: 36px; top: 58px; width: 240px;
    font-weight: 800; font-size: 30px; line-height: 1.1;
    color: var(--ink);
  }
  .intro {
    left: 36px; top: 150px; width: 230px;
    font-size: 14px; line-height: 1.35; color: var(--ink);
  }
  .brand-name {
    left: 36px; top: 240px;
    font-family: "Oswald", "Arial Narrow", sans-serif;
    font-weight: 500; font-size: 30px; letter-spacing: 0.5px;
    color: var(--logo-blue); text-transform: uppercase;
  }

  .program-title {
    left: 44px; top: 366px;
    font-family: "Oswald", "Arial Narrow", sans-serif;
    font-weight: 700; font-size: 44px; line-height: 1;
    color: var(--paper);
  }
  .program-title .accent { display: block; color: var(--lime); }

  .feature-list {
    list-style: none;
    font-size: 11px; line-height: 1.45; color: var(--paper);
  }
  .kickstart-list { left: 44px; top: 466px; width: 262px; }

  .benefits-title {
    left: 330px; top: 350px;
    font-family: "Oswald", "Arial Narrow", sans-serif;
    font-weight: 700; font-size: 30px; color: var(--lime);
  }
  .benefits-list { left: 330px; top: 400px; width: 250px; }

  .price-offer {
    left: 330px; top: 496px; width: 270px;
    font-weight: 700; font-size: 19px; line-height: 1.3;
    color: var(--lime);
  }

  .tagline {
    left: 44px; top: 596px; width: 560px;
    font-weight: 700; font-size: 15px; letter-spacing: 2px;
    color: var(--paper);
  }
  .tagline .accent { color: var(--lime); }
</style>
</head>
<body>
  <article class="flyer">
    <svg class="flyer-shapes" viewBox="0 0 620 800">
      <defs>
        <linearGradient id="photo-tone" x1="0" y1="0" x2="1" y2="1">
          <stop offset="0" stop-color="#5a56c8"/>
          <stop offset="0.55" stop-color="#4a4660"/>
          <stop offset="1" stop-color="#2a2b3a"/>
        </linearGradient>
      </defs>
      <rect class="hero-photo" x="0" y="0" width="620" height="345" fill="url(#photo-tone)"
            role="img" aria-label="Photo of women doing squats in a group fitness class"/>
      <polygon class="blue-band" points="0,345 620,290 620,800 0,800" fill="var(--brand-blue)"/>
      <polygon class="intro-panel" points="0,0 280,0 415,120 260,322 0,345" fill="var(--lime)"/>
      <polygon class="corner-block" points="0,690 160,690 186,760 186,800 0,800" fill="var(--lime)"/>
      <polygon class="paper-block" points="186,770 330,695 520,705 410,800 186,800" fill="var(--paper)"/>
      <g class="chevrons-right" fill="var(--lime)">
        <polygon points="200,632 222,632 246,657 222,682 200,682 224,657"/>
        <polygon points="232,632 254,632 278,657 254,682 232,682 256,657"/>
        <polygon points="264,632 286,632 310,657 286,682 264,682 288,657"/>
      </g>
      <g class="chevrons-left" fill="var(--lime)">
        <polygon points="566,350 588,350 564,375 588,400 566,400 542,375"/>
        <polygon points="598,350 620,350 596,375 620,400 598,400 574,375"/>
      </g>
    </svg>

    <h1 class="flyer-text headline">Change Begins NOW!</h1>
    <p class="flyer-text intro">The Fitness Program that is responsible for transforming over 924+ lives!</p>
    <div class="flyer-text brand-name">Northline Fitness</div>

    <h2 class="flyer-text program-title">The Ultimate <span class="accent">Kickstart</span></h2>
    <ul class="flyer-text feature-list kickstart-list">
      <li>(2) Detailed Body Scans to track results</li>
      <li>Supplement List to accelerate metabolism</li>
      <li>10% off First Supplement Purchase to Kickstart the process</li>
      <li>Exclusive access to Northline's Private Members Hub Page for additional recipes, Support and Guidance</li>
    </ul>

    <h2 class="flyer-text benefits-title">What you get</h2>
    <ul class="flyer-text feature-list benefits-list">
      <li>Unlimited Group Training Designed Specifically to Sculpt &amp; Tone the body.</li>
      <li>CUSTOM Meal Plan designed specifically for Your and Your Body Type</li>
    </ul>

    <p class="flyer-text price-offer">Get started for $199 (crossed out) ONLY $99limited time</p>

    <p class="flyer-text tagline">The Life That You Envision IS <span class="accent">POSSIBLE!</span></p>
  </article>
</body>
</html>
```